Internal Office Slogans / Motto / Vision Statements

Hi. We would like to put up some posters around the office with quotations such as -
-”Do what you do so well that they will want to see it again and bring their friends.”- Hollis Trevane
-Make your customers feel heard and understood. Make your customers feel respected and liked. Make your customers feel appreciated and helped. Understand that you can do none of these things unless you are sincere about them.
Gregory Pilcott
- It’s a very predictable and satisfying phenomenon: whenever we get better, our customers do too.
Ray Casso
-Catch people in the act of performing extraordinary customer service. Treat them like heroes. Tell their stories, far and wide.
Tod Brinkerley

The purpose of the posters is to reiterate our culture and vision within the organisation. They should be clean, crisp and eye catching, not gaudy or bright. Professional, bold and strong.

The company website and logo is at http://www.nexolux.com.au
Print size will be A1

Thanks for participating & looking forward to seeing your great work.
Updates

Hi All. . 

So to reiterate we are looking for one background design to be used for multiple quotes...  The list of quotes are as follows: 

Support and or Sales Office

 

Make your customers feel heard and understood.Make your customers feel respected and liked. Make your customers feelappreciated and helped. Understand that you can do none of these things unlessyou are sincere about them.

Gregory Pilcott

 

Nothing liberates our greatness like the desireto help, the desire to serve

Rosalind Penhallow

 

It’s a very predictable and satisfying phenomenon:whenever we get better, our customers do too.

Ray Casso

 

Success means we go to sleep at night knowingthat our talents and abilities were used in a way that served others.

Rosalind Penhallow.

 

The sole purpose of business is to create, serveand satisfy a customer, from beginning to end – and that’s everyone’s job.

Tod Brinkerley

 

We don’t celebrate closing a sale, we celebrateopening a relationship.

Gwendolyn Asque

I will never make you a promise – unless I giveyou a plan and procedure to make that promise possible.

Bo Tarrick

 

Customers feel we take them for granted; onlyshow interest when we want an order; lavish our time on prospects; communicatemainly by invoice; are fixated on big accounts; drop them like hot potatoesonce we have the order; don’t follow through on promises; and satisfy our ownbureaucracy rather than their needs. We can do better than that, much better.

Peter L Osmund.

 

 

General and public area

 

Catch people in the act of performingextraordinary customer service. Treat them like heroes. Tell their stories, farand wide.

Tod Brinkerley

 

 

We see our customers as invited guests to aparty, and we are the hosts. It’s our job every day to make every importantaspect of the customer experience a little bit better." Carl Ingvold - Founder andCEO of Veltrix

 

"If you do build a great experience,customers tell each other about that. Word of mouth is verypowerful."  Carl Ingvold

 

It's not a faithin technology. It's faith in people. Neil Corrby

 

“Being the richest man in the cemetery doesn’tmatter to me … Going to bed at night saying we’ve done something wonderful…that’s what matters to me.” Neil Corrby

 

The customer experience is the next competitivebattleground. Lance Merriwether, CIO, Quorra Computers

 

”Do what you do so well that they will want tosee it again and bring their friends.”- Hollis Trevane

In the world of internet customer service, it isimportant to remember your competitor is only a mouse click away. GlenTrasky (not sure who he is but like the quote).

The customer is why you go to work. If they goaway, you do, too. Martin Glossop (?)

 

MaybeSome for Sales or Build Team:

Quality is remembered long after the price is forgotten. Varenne Family Slogan

```html
<!DOCTYPE html>
<html lang="en">
<head>
<meta charset="utf-8">
<title>Nexolux – Customer Quote Poster</title>
<link rel="stylesheet" href="https://fonts.googleapis.com/css2?family=Arimo:ital,wght@0,700;1,400&display=swap">
<style>
  :root {
    --bg-top: #36434b;
    --bg-mid: #2b353c;
    --bg-bottom: #1e262b;
    --brand-red: #c8000b;
    --text-white: #ffffff;
  }
  html, body {
    margin: 0;
    padding: 0;
    overflow: hidden;
    background: var(--bg-bottom);
  }
  .poster {
    position: relative;
    width: 848px;
    height: 1200px;
    overflow: hidden;
    font-family: "Arimo", Arial, sans-serif;
    color: var(--text-white);
  }
  .poster-background {
    position: absolute;
    inset: 0;
    background:
      radial-gradient(ellipse at 50% 35%, var(--bg-top) 0%, var(--bg-mid) 55%, var(--bg-bottom) 100%);
  }
  .brand {
    position: absolute;
    left: 64px;
    top: 53px;
    display: flex;
    align-items: center;
    gap: 8px;
  }
  .brand-square {
    width: 43px;
    height: 43px;
    background: var(--brand-red);
  }
  .brand-name {
    font-weight: 700;
    font-size: 46px;
    line-height: 1;
    letter-spacing: -1px;
    color: var(--text-white);
  }
  .quote-mark {
    position: absolute;
    fill: var(--brand-red);
  }
  .quote-mark--open {
    left: 73px;
    top: 273px;
    width: 230px;
    height: 182px;
  }
  .quote-mark--close {
    left: 553px;
    top: 893px;
    width: 230px;
    height: 182px;
  }
  .quote-text {
    position: absolute;
    left: 129px;
    top: 330px;
    margin: 0;
    font-weight: 700;
    font-size: 48px;
    line-height: 62px;
    letter-spacing: 0.2px;
    white-space: nowrap;
  }
  .quote-author {
    position: absolute;
    right: 104px;
    top: 1038px;
    margin: 0;
    font-style: italic;
    font-weight: 400;
    font-size: 12px;
  }
</style>
</head>
<body>
<main class="poster">
  <div class="poster-background" role="img" aria-label="Dark slate knitted fabric texture background"></div>

  <header class="brand">
    <span class="brand-square"></span>
    <span class="brand-name">Nexolux</span>
  </header>

  <svg class="quote-mark quote-mark--open" viewBox="0 0 230 182" aria-hidden="true">
    <path d="M0 182 L0 112 C0 56 28 16 78 0 L88 16 C58 32 46 56 46 82 L92 82 L92 182 Z"/>
    <path d="M122 182 L122 112 C122 56 150 16 200 0 L210 16 C180 32 168 56 168 82 L214 82 L214 182 Z"/>
  </svg>

  <svg class="quote-mark quote-mark--close" viewBox="0 0 230 182" aria-hidden="true">
    <g transform="rotate(180 115 91)">
      <path d="M0 182 L0 112 C0 56 28 16 78 0 L88 16 C58 32 46 56 46 82 L92 82 L92 182 Z"/>
      <path d="M122 182 L122 112 C122 56 150 16 200 0 L210 16 C180 32 168 56 168 82 L214 82 L214 182 Z"/>
    </g>
  </svg>

  <p class="quote-text">Make your customers<br>
feel heard and<br>
understood. Make your<br>
customers feel<br>
respected and liked.<br>
Make your customers<br>
feelappreciated and<br>
helped. Understand that<br>
you can do none of<br>
these things unlessyou<br>
are sincere about them.</p>

  <p class="quote-author">(Gregory Pilcott)</p>
</main>
</body>
</html>
```